brolvin business card design so that it looks better

need a new business card designed. use our website, brolvix.example for example. I attached an example of a previous card we had and liked. this is for law enforcement and we have attached a previous business card as an example. This site forces me to select color and font, ignore those as I picked stuff just to get this completed.

Target Market(s)

law enforcement, local government

Contact Information for Business Card

see the attached example and our website

Font styles to use
Serif

```html
<!DOCTYPE html>
<html lang="en">
<head>
<meta charset="utf-8">
<title>brolvin business card</title>
<link rel="stylesheet" href="https://fonts.googleapis.com/css2?family=Raleway:wght@300&family=Poppins:wght@500&display=swap">
<style>
  :root {
    --page: #e9e7e4;
    --navy-deep: #061521;
    --navy: #0b2236;
    --network-blue: #1c5fa8;
    --glow: #3fa9e8;
    --band: #1f6db5;
    --band-edge: #1a5d9c;
    --ink-light: #f4f7fb;
  }
  * { box-sizing: border-box; margin: 0; padding: 0; }
  html, body { width: 1200px; height: 1200px; overflow: hidden; background: var(--page); }
  .canvas {
    width: 1200px; height: 1200px;
    display: flex; flex-direction: column; align-items: center; justify-content: center; gap: 60px;
  }
  .card {
    position: relative; width: 840px; height: 480px; overflow: hidden;
    background: var(--navy-deep);
    box-shadow: 0 14px 30px rgba(0,0,0,0.18);
  }
  /* Front */
  .card-front .network-art {
    position: absolute; inset: 0;
    background:
      radial-gradient(ellipse 55% 45% at 45% 78%, rgba(40,110,200,0.55), transparent 70%),
      radial-gradient(ellipse 40% 35% at 80% 30%, rgba(30,90,170,0.35), transparent 70%),
      linear-gradient(160deg, #071624 0%, #0a2034 55%, #0d2a48 100%);
  }
  .card-front .brand-name {
    position: absolute; left: 230px; top: 150px;
    font-family: "Raleway", sans-serif; font-weight: 300;
    font-size: 112px; letter-spacing: 4px; line-height: 1;
    color: var(--ink-light);
  }
  /* Back */
  .card-back { background: linear-gradient(180deg, var(--navy-deep) 0%, var(--navy) 100%); }
  .card-back .map-art {
    position: absolute; left: 200px; top: 70px; width: 520px; height: 330px;
    border-radius: 40% 46% 38% 50% / 42% 38% 55% 48%;
    background:
      radial-gradient(circle at 68% 72%, rgba(80,200,230,0.55), transparent 35%),
      radial-gradient(ellipse at 50% 50%, rgba(40,110,170,0.45), rgba(10,40,70,0.2) 75%);
  }
  .card-back .band-edge {
    position: absolute; left: 0; right: 0; height: 4px; background: var(--band-edge);
  }
  .card-back .band-edge.top { top: 170px; }
  .card-back .band-edge.bottom { top: 300px; }
  .card-back .band {
    position: absolute; left: 0; right: 0; top: 180px; height: 112px;
    background: var(--band);
    display: flex; align-items: center; justify-content: flex-end; padding-right: 190px;
  }
  .card-back .web-address {
    font-family: "Poppins", sans-serif; font-weight: 500;
    font-size: 34px; letter-spacing: 0.5px; color: var(--ink-light);
  }
</style>
</head>
<body>
<main class="canvas">
  <section class="card card-front">
    <div class="network-art" role="img" aria-label="Glowing blue network of connected points across a dark navy background"></div>
    <h1 class="brand-name">BROLVIN</h1>
  </section>

  <section class="card card-back">
    <div class="map-art" role="img" aria-label="Map of the United States drawn as a glowing network of connected points"></div>
    <div class="band-edge top"></div>
    <div class="band"><p class="web-address">WWW.BROLVIX.EXAMPLE</p></div>
    <div class="band-edge bottom"></div>
  </section>
</main>
</body>
</html>
```